UI/ UX Design for ERP Software

We need a new UX/UI interface for a ERP software for property managers. Our CMMS / ERP solution is made based on responsive design technologies and is coded in PHP.
The overall UX to be similar to Zel Kavo - easy navigation, intuitive menus.

Industry/Entity Type

Property Management

Number of Pages Required

5+ page

Requirements
Must have
• Round dock buttons
Consistent icons across the application
Enough Spacing between buttons/icons/ menu
Consistent Font
Nice to have
• We would like the UX to allow the users to use the application without /minimum training.
Should not have
• we don't want anything that is classic with respect to UX

```html
<!DOCTYPE html>
<html lang="en">
<head>
<meta charset="utf-8">
<title>Keyhold – Maintenance calendar</title>
<link href="https://fonts.googleapis.com/css2?family=Inter:wght@400;500;600;700&display=swap" rel="stylesheet">
<style>
:root{
  --page-bg:#f6f9fc;
  --card:#ffffff;
  --ink:#1c2430;
  --muted:#5d6b7a;
  --line:#e3e8ef;
  --blue:#0d84e8;
  --blue-bright:#1a93f0;
  --orange:#f2703f;
  --panel:#f1f5fa;
  --past:#e3f0f9;
  --past-ink:#6a7c8c;
}
*{box-sizing:border-box;margin:0;padding:0}
html,body{width:1200px;height:1200px;overflow:hidden;background:var(--page-bg);font-family:'Inter',sans-serif;color:var(--ink)}
.app-window{position:absolute;left:188px;top:62px;width:826px;height:1076px;background:var(--card);border-radius:22px;box-shadow:0 10px 40px rgba(30,60,100,.07)}
.window-dots{position:absolute;left:25px;top:5px;display:flex;gap:5px}
.window-dots span{width:6px;height:6px;border-radius:50%}
.brand{position:absolute;left:24px;top:34px;display:flex;align-items:center;gap:5px;font-size:13px;font-weight:600;color:var(--blue)}
.brand-mark{width:10px;height:10px;background:var(--blue);border-radius:2px}
.refresh-btn{position:absolute;left:103px;top:30px;width:98px;height:25px;border-radius:6px;background:#fff;box-shadow:0 2px 10px rgba(30,60,100,.08);display:flex;align-items:center;justify-content:center;gap:4px;font-size:7.5px;font-weight:500;color:#1d3a5c}
.breadcrumb{position:absolute;left:216px;top:36px;font-size:9.5px;color:var(--ink)}
.breadcrumb b{font-weight:600}
.user{position:absolute;right:28px;top:27px;display:flex;align-items:center;gap:11px;font-size:9.5px}
.user b{font-weight:600}
.avatar{width:31px;height:31px;border-radius:50%;background:linear-gradient(135deg,#6b4a3a,#c89a7e)}
.page-title{position:absolute;left:29px;top:70px;display:flex;align-items:center;gap:8px;font-size:14px;font-weight:600}
.back-btn{width:13px;height:13px;border-radius:50%;background:var(--ink);display:flex;align-items:center;justify-content:center}
.property-tabs{position:absolute;left:29px;top:104px;display:flex;gap:4.5px}
.property-tab{width:86px;height:25px;border:1px solid var(--line);border-radius:4px;font-size:7px;font-weight:500;display:flex;align-items:center;justify-content:center}
.view-switch{position:absolute;left:29px;top:145px;display:flex}
.view-btn{height:37px;display:flex;align-items:center;gap:5px;font-size:8.5px;font-weight:600;border-radius:4px}
.view-btn.requests{width:131px;background:var(--panel);padding-left:22px}
.view-btn.schedule{width:144px;background:var(--blue-bright);color:#fff;justify-content:center;margin-left:6px;box-shadow:0 4px 12px rgba(26,147,240,.3)}
.month-nav{position:absolute;right:28px;top:198px;display:flex;align-items:center}
.month-label{font-size:14px;font-weight:600;margin-right:21px}
.nav-btn{width:24px;height:23px;border-radius:3px;display:flex;align-items:center;justify-content:center}
.nav-btn.prev{background:#e1edf6;margin-right:14px}
.nav-btn.next{background:#fff;box-shadow:0 2px 8px rgba(30,60,100,.1)}
.month-grid{position:absolute;left:25px;top:233px;width:773px;height:737px;background:var(--panel);border-radius:8px;padding:0 11px}
.weekdays{display:grid;grid-template-columns:repeat(7,103px);column-gap:5px;height:35px;align-items:center;text-align:center;font-size:11px;font-weight:600}
.days{display:grid;grid-template-columns:repeat(7,103px);grid-auto-rows:165px;gap:6px 5px}
.day{position:relative;background:#fff;border:1px solid var(--line)}
.day.outside{background:var(--past);border-color:#d5e6f2}
.day-num{position:absolute;right:7px;top:9px;font-size:9px;font-weight:600}
.day.outside .day-num{color:var(--past-ink)}
.event{position:absolute;left:0;right:0;height:26px;padding:3px 7px;font-size:6.6px;font-weight:500;line-height:1.45;color:#fff;white-space:nowrap;overflow:hidden}
.event.blue{background:var(--blue)}
.event.orange{background:var(--orange)}
.event.e1{top:30px}.event.e2{top:66px}
.first-row .event.e1{top:40px}.first-row .event.e2{top:76px}
.dock{position:absolute;left:347px;top:998px;width:131px;height:50px;background:#fff;border-radius:10px;box-shadow:0 4px 18px rgba(30,60,100,.07);display:flex;align-items:center;justify-content:center;gap:27px}
.dock-btn{width:35px;height:35px;border-radius:9px;display:flex;align-items:center;justify-content:center}
.dock-btn.home{background:linear-gradient(180deg,#1aa3f5,#0d7fe6)}
.dock-btn.apps{background:linear-gradient(180deg,#ff9a3d,#f26a2e)}
</style>
</head>
<body>
<div class="app-window">
  <div class="window-dots"><span style="background:#f7c948"></span><span style="background:#f2545b"></span><span style="background:#4cd87a"></span></div>
  <div class="brand"><span class="brand-mark"></span>Keyhold</div>
  <div class="refresh-btn"><svg width="8" height="8" viewBox="0 0 10 10"><path d="M8 5a3 3 0 1 1-1-2.2" fill="none" stroke="#1d3a5c" stroke-width="1.4"/><path d="M6 1h2.5v2.5" fill="none" stroke="#1d3a5c" stroke-width="1.4"/></svg>Refresh this page</div>
  <div class="breadcrumb"><b>Home</b> &nbsp;/&nbsp; Properties</div>
  <div class="user"><span>Welcome, <b>Rhea Dalton</b></span><div class="avatar" role="img" aria-label="User profile photo"></div></div>

  <div class="page-title">
    <span class="back-btn"><svg width="6" height="6" viewBox="0 0 6 6"><path d="M4 1L2 3l2 2" fill="none" stroke="#fff" stroke-width="1.2"/></svg></span>
    <svg width="16" height="16" viewBox="0 0 16 16" fill="none" stroke="#1c2430" stroke-width="1.1"><rect x="1.5" y="1.5" width="8" height="13"/><rect x="9.5" y="6" width="5" height="8.5"/><path d="M3.5 4h4M3.5 6.5h4M3.5 9h4M11 8.5h2M11 11h2M4.5 14.5v-3h2v3"/></svg>
    Properties list
  </div>

  <div class="property-tabs">
    <div class="property-tab">Prime tower</div><div class="property-tab">Prime tower</div><div class="property-tab">Prime tower</div><div class="property-tab">Prime tower</div><div class="property-tab">Prime tower</div><div class="property-tab">Prime tower</div><div class="property-tab">Prime tower</div>
  </div>

  <div class="view-switch">
    <div class="view-btn requests"><svg width="10" height="11" viewBox="0 0 10 11" fill="none" stroke="#1c2430" stroke-width="1.1"><rect x="1" y="1.5" width="8" height="9" rx="1"/><path d="M3.5 1h3"/></svg>Request / orders</div>
    <div class="view-btn schedule"><svg width="10" height="10" viewBox="0 0 10 10" fill="none" stroke="#fff" stroke-width="1"><rect x="0.8" y="1.5" width="8.4" height="7.7" rx="1"/><path d="M0.8 4h8.4M3 0.5v2M7 0.5v2"/></svg>Maintenance calendar</div>
  </div>

  <div class="month-nav">
    <span class="month-label">January 2021</span>
    <span class="nav-btn prev"><svg width="7" height="9" viewBox="0 0 7 9"><path d="M5 1L2 4.5 5 8" fill="none" stroke="#5b84a8" stroke-width="1.5"/></svg></span>
    <span class="nav-btn next"><svg width="7" height="9" viewBox="0 0 7 9"><path d="M2 1l3 3.5L2 8" fill="none" stroke="#1c2430" stroke-width="1.5"/></svg></span>
  </div>

  <section class="month-grid">
    <div class="weekdays"><span>Sunday</span><span>Monday</span><span>Tuesday</span><span>Wednesday</span><span>Thursday</span><span>Friday</span><span>Saturday</span></div>
    <div class="days">
      <div class="day outside first-row"><span class="day-num">27</span></div>
      <div class="day outside first-row"><span class="day-num">28</span></div>
      <div class="day outside first-row"><span class="day-num">29</span></div>
      <div class="day outside first-row"><span class="day-num">30</span></div>
      <div class="day outside first-row"><span class="day-num">31</span></div>
      <div class="day first-row"><span class="day-num">01</span><div class="event blue e1">Maintenance Prime tower<br>6:00</div><div class="event orange e2">Maintenance Prime tower<br>6:00</div></div>
      <div class="day first-row"><span class="day-num">02</span></div>

      <div class="day"><span class="day-num">03</span></div>
      <div class="day"><span class="day-num">04</span></div>
      <div class="day"><span class="day-num">05</span></div>
      <div class="day"><span class="day-num">06</span></div>
      <div class="day"><span class="day-num">07</span><div class="event blue e1">Maintenance Prime tower<br>6:00</div><div class="event orange e2">Maintenance Prime tower<br>6:00</div></div>
      <div class="day"><span class="day-num">08</span></div>
      <div class="day"><span class="day-num">09</span></div>

      <div class="day"><span class="day-num">10</span></div>
      <div class="day"><span class="day-num">11</span><div class="event blue e1">Maintenance Prime tower<br>6:00</div></div>
      <div class="day"><span class="day-num">12</span><div class="event blue e1">Maintenance Prime tower<br>6:00</div></div>
      <div class="day"><span class="day-num">13</span></div>
      <div class="day"><span class="day-num">14</span><div class="event blue e1">Maintenance Prime tower<br>6:00</div><div class="event orange e2">Maintenance Prime tower<br>6:00</div></div>
      <div class="day"><span class="day-num">15</span></div>
      <div class="day"><span class="day-num">16</span><div class="event blue e1">Maintenance Prime tower<br>6:00</div><div class="event orange e2">Maintenance Prime tower<br>6:00</div></div>

      <div class="day"><span class="day-num">17</span><div class="event blue e1">Maintenance Prime tower<br>6:00</div><div class="event orange e2">Maintenance Prime tower<br>6:00</div></div>
      <div class="day"><span class="day-num">18</span></div>
      <div class="day"><span class="day-num">19</span><div class="event blue e1">Maintenance Prime tower<br>6:00</div><div class="event orange e2">Maintenance Prime tower<br>6:00</div></div>
      <div class="day"><span class="day-num">20</span></div>
      <div class="day"><span class="day-num">21</span></div>
      <div class="day"><span class="day-num">22</span><div class="event blue e1">Maintenance Prime tower<br>6:00</div><div class="event orange e2">Maintenance Prime tower<br>6:00</div></div>
      <div class="day"><span class="day-num">23</span></div>
    </div>
  </section>

  <nav class="dock">
    <span class="dock-btn home"><svg width="14" height="13" viewBox="0 0 14 13"><path d="M7 1L1 6v6h4V8.5h4V12h4V6z" fill="#fff"/></svg></span>
    <span class="dock-btn apps"><svg width="14" height="14" viewBox="0 0 14 14" fill="#fff"><circle cx="2" cy="2" r="1.4"/><circle cx="7" cy="2" r="1.4"/><circle cx="12" cy="2" r="1.4"/><circle cx="2" cy="7" r="1.4"/><circle cx="7" cy="7" r="1.4"/><circle cx="12" cy="7" r="1.4"/><circle cx="2" cy="12" r="1.4"/><circle cx="7" cy="12" r="1.4"/><circle cx="12" cy="12" r="1.4"/></svg></span>
  </nav>
</div>
</body>
</html>
```